Social Media Graphics - ALL TEXT RK

We are looking for a series of social media graphics for Instagram (standard size 1:1 (1080x1080px) that are ALL TEXT. We want the following quotes below on each graphic; one quote per graphic. AND, In very small letters at the bottom of each graphic, add @RKMarlowLive

The look and feel of these graphics should be complimentary to the color palette attached below; but keep them simple. But the design is up to you; at the end of this document, I provided various samples of all text graphics that I like as examples.

Target Market(s)

women looking to lose weight

Industry/Entity Type

health and wellness

Colors
E54698
E96AAD
F1A4CE
F9D9EA
FCEFF6

Requirements
Must have
• the quotes in the document
Should not have
• no stock photography

```html
<!DOCTYPE html>
<html lang="en">
<head>
<meta charset="utf-8">
<title>Overnight Flat Belly Quote</title>
<link rel="stylesheet" href="https://fonts.googleapis.com/css2?family=Montserrat:wght@500;800&display=swap">
<style>
  :root {
    --plum-deep: #5e0a5a;
    --magenta: #b0066f;
    --pink-hot: #e5077c;
    --pink-bright: #f0107f;
    --white: #ffffff;
  }
  html, body {
    margin: 0;
    padding: 0;
    width: 1200px;
    height: 1200px;
    overflow: hidden;
  }
  .post {
    position: relative;
    width: 1200px;
    height: 1200px;
    overflow: hidden;
    background:
      radial-gradient(circle at 85% 20%, rgba(255, 80, 170, 0.35) 0, rgba(255, 80, 170, 0) 45%),
      radial-gradient(circle at 20% 85%, rgba(255, 60, 160, 0.25) 0, rgba(255, 60, 160, 0) 40%),
      linear-gradient(135deg, var(--plum-deep) 0%, var(--magenta) 38%, var(--pink-hot) 72%, var(--pink-bright) 100%);
    font-family: "Montserrat", Arial, sans-serif;
    color: var(--white);
  }
  .frame {
    position: absolute;
    left: 0;
    top: 0;
  }
  .quote {
    position: absolute;
    left: 298px;
    top: 290px;
    margin: 0;
    font-weight: 800;
    font-size: 76px;
    line-height: 86px;
    letter-spacing: 1.5px;
    text-transform: uppercase;
  }
  .handle {
    position: absolute;
    left: 0;
    right: 0;
    top: 1104px;
    margin: 0;
    text-align: center;
    font-weight: 500;
    font-size: 31px;
    letter-spacing: 1px;
  }
</style>
</head>
<body>
  <main class="post">
    <svg class="frame" width="1200" height="1200" viewBox="0 0 1200 1200" aria-hidden="true">
      <rect x="132" y="110" width="951" height="937" fill="none" stroke="var(--white)" stroke-width="3.5"/>
    </svg>
    <h1 class="quote">Wake up<br>tomorrow<br>with a flatter<br>belly- yes,<br>this overnight<br>remedy works<br>like magic!</h1>
    <p class="handle">@RKMarlowLive</p>
  </main>
</body>
</html>
```